Lom Consulting -New consulting business in architecture, urban planning, and real estate development

We need a stationery design, including logo, business cards, etc, work for a new consulting business that works in the world of architectural, urban planning and real estate development.

The name of the company is "Lom Consulting". Lom is my last name but it of course also has the meaning 'cool' and 'hip'.

Target Market(s)

The business will provide boutique consulting services to high end clients that may include property developers, cities, etc.

Industry/Entity Type

Consultant

Contact Information for Business Card

LOM Consulting
First Name Last Name
Title
Phone number
Address
Website
Optional: Twitter handle

Logo Text

LOM Consulting

Font styles to use
Sans Serif

Colors

Designer to choose colors to be used in the design.

Requirements
Must have
• Simple design
• Easy to read font
• Modern
• Elegance
• Nice font that can be used for future reports, letters, etc.
• Good colour scheme that allows for the elegance to come through
Should not have
• Complex design ideas
• Complex logos
• Not a corporate feel and look

```html
<!DOCTYPE html>
<html lang="en">
<head>
<meta charset="utf-8">
<title>LOM Consulting – Business Cards</title>
<link href="https://fonts.googleapis.com/css2?family=Roboto:wght@300;400;700;900&display=swap" rel="stylesheet">
<style>
  :root{
    --navy-deep:#141f55;
    --navy:#22337f;
    --blue:#3a55a8;
    --orange:#f08a12;
    --orange-deep:#e8680c;
    --white:#ffffff;
    --ink:#1b1b1b;
    --bg:#e9e7e3;
  }
  *{margin:0;padding:0;box-sizing:border-box}
  html,body{width:1200px;height:1200px;overflow:hidden;background:var(--bg);font-family:"Roboto",sans-serif}
  .canvas{position:relative;width:1200px;height:1200px}
  .card{position:absolute;left:220px;width:760px;height:434px;overflow:hidden;box-shadow:0 14px 36px rgba(0,0,0,.22)}
  .card--front{top:130px}
  .card--back{top:636px;background:var(--white)}
  .card svg.shapes{position:absolute;inset:0;width:100%;height:100%}
  .wordmark{position:absolute;display:flex;align-items:center;gap:14px;font-family:"Roboto",sans-serif;font-weight:900;line-height:1}
  .wordmark__dot{width:46px;height:46px;border-radius:50%;background:var(--orange)}
  .wordmark__text{display:flex;flex-direction:column}
  .wordmark__main{font-size:64px;letter-spacing:4px}
  .wordmark__sub{font-size:17px;letter-spacing:6px;margin-top:4px}
  .card--front .wordmark{left:250px;top:160px;color:var(--white)}
  .card--back .wordmark{left:470px;top:30px;color:var(--navy)}
  .card--back .wordmark__dot{width:38px;height:38px}
  .card--back .wordmark__main{font-size:50px}
  .card--back .wordmark__sub{font-size:14px;letter-spacing:5px}
  .holder{position:absolute;left:60px;top:190px;font-size:22px;color:var(--ink);font-weight:300;letter-spacing:.5px}
  .holder strong{font-weight:900}
  .contact{position:absolute;color:var(--white);font-size:15px;line-height:1.45;font-weight:400}
  .contact svg{display:block;margin-bottom:8px}
  .contact--phone{left:70px;top:264px}
  .contact--address{left:360px;top:198px}
  .contact--web{left:590px;top:138px}
</style>
</head>
<body>
<main class="canvas">

  <section class="card card--front" aria-label="Business card front">
    <svg class="shapes" viewBox="0 0 760 434" preserveAspectRatio="none">
      <defs>
        <linearGradient id="frontFill" x1="0" y1="0" x2="0.4" y2="1">
          <stop offset="0" stop-color="#3a55a8"/>
          <stop offset="1" stop-color="#141f55"/>
        </linearGradient>
        <radialGradient id="mapHaze" cx="0.5" cy="0.5" r="0.5">
          <stop offset="0" stop-color="#1a2870" stop-opacity=".6"/>
          <stop offset="1" stop-color="#1a2870" stop-opacity="0"/>
        </radialGradient>
      </defs>
      <rect width="760" height="434" fill="url(#frontFill)"/>
      <ellipse cx="400" cy="180" rx="340" ry="150" fill="url(#mapHaze)" role="img" aria-label="Faint world map in the background"/>
      <polygon points="430,352 760,238 760,300 470,400" fill="var(--orange)"/>
      <polygon points="430,352 470,400 760,300 760,330 480,420" fill="var(--orange-deep)"/>
    </svg>
    <div class="wordmark">
      <span class="wordmark__dot"></span>
      <span class="wordmark__text"><span class="wordmark__main">LOM</span><span class="wordmark__sub">CONSULTING</span></span>
    </div>
  </section>

  <section class="card card--back" aria-label="Business card back">
    <svg class="shapes" viewBox="0 0 760 434" preserveAspectRatio="none">
      <defs>
        <linearGradient id="bandFill" x1="0" y1="1" x2="1" y2="0">
          <stop offset="0" stop-color="#141f55"/>
          <stop offset="0.55" stop-color="#22337f"/>
          <stop offset="1" stop-color="#3a55a8"/>
        </linearGradient>
      </defs>
      <polygon points="0,268 760,88 760,296 0,400" fill="url(#bandFill)"/>
      <polygon points="405,345 760,296 760,350 440,396" fill="var(--orange)"/>
    </svg>

    <div class="wordmark">
      <span class="wordmark__dot"></span>
      <span class="wordmark__text"><span class="wordmark__main">LOM</span><span class="wordmark__sub">CONSULTING</span></span>
    </div>

    <p class="holder"><strong>NAME</strong>SURNAME</p>

    <div class="contact contact--phone">
      <svg width="34" height="34" viewBox="0 0 34 34" aria-hidden="true">
        <circle cx="17" cy="17" r="15.5" fill="none" stroke="#fff" stroke-width="2"/>
        <path d="M12 9c2 0 3 3 3 4s-2 1-1.5 3 2 3.5 3.5 4 1.5-1.5 2.5-1.5 4 1 4 3-2 3-3.5 3C14 24.5 9.5 20 9.5 13.5 9.5 11 10.5 9 12 9z" fill="#fff"/>
      </svg>
      +61 1.800.555.0142<br>+61 1.800.555.0142
    </div>

    <div class="contact contact--address">
      <svg width="26" height="34" viewBox="0 0 26 34" aria-hidden="true">
        <path d="M13 1C6.4 1 1.5 6 1.5 12.3 1.5 20 13 33 13 33s11.5-13 11.5-20.7C24.5 6 19.6 1 13 1z" fill="#fff"/>
        <circle cx="13" cy="12.5" r="4.5" fill="#22337f"/>
      </svg>
      Level 3, 18 Elm Lane<br>Redfern 2016 Australia
    </div>

    <div class="contact contact--web">
      <svg width="34" height="34" viewBox="0 0 34 34" aria-hidden="true" fill="none" stroke="#fff" stroke-width="2">
        <circle cx="17" cy="17" r="15"/>
        <ellipse cx="17" cy="17" rx="7" ry="15"/>
        <line x1="2" y1="17" x2="32" y2="17"/>
        <line x1="5" y1="9" x2="29" y2="9"/>
        <line x1="5" y1="25" x2="29" y2="25"/>
      </svg>
      www.lomconsult.com<br>info@lomconsult.com
    </div>
  </section>

</main>
</body>
</html>
```